Customer Journey Graphic

I want to graphic to describe a marketing framework I am teaching a course on

It a framework for growing a business
The idea is we
get customers to "take a Journey" through 7 steps
to deliver value to them

There are 4 major concepts that impact this journey - Game Plan, Business Model, "Inside out thinking' and Unique Competitive advantage
These concepts can make the journey faster, get more people to take it or make it more valuable

The stages are

- Target
- attract
- nurture
- convert
- maximise
- loyalty
- reactivation

I want to uses this framework as an overall;; 'explainer' fro my idea ,so it must looks very professional, and work well in presentations

I have included a rought 'sketch; of my thinking as an attachment
Updates

Target Market(s)

Business Owners

Industry/Entity Type

Business

Font styles to use
Serif

Requirements
Must have
• clear, get acroess the idea of a Journye over times, teh idea you can improve your results throught applying concpets of ' business model', "inside out thinking: , unique competitive advantage and game plane

```html
<!DOCTYPE html>
<html lang="en">
<head>
<meta charset="utf-8">
<title>Customer Journey Framework</title>
<link href="https://fonts.googleapis.com/css2?family=Courier+Prime:wght@700&display=swap" rel="stylesheet">
<style>
  :root {
    --bg: #ffffff;
    --red: #f66353;
    --red-shade: #e4483b;
    --orange: #eb6424;
    --green: #97c43f;
    --green-shade: #6f8f31;
    --teal: #12b9bc;
    --teal-shade: #0e9ea1;
    --tile: #553f3b;
    --ink: #ffffff;
  }
  html, body {
    margin: 0;
    padding: 0;
    width: 1200px;
    height: 800px;
    overflow: hidden;
    background: var(--bg);
  }
  .journey-canvas {
    display: block;
    width: 1200px;
    height: 800px;
  }
  .concept-label {
    font-family: "Courier Prime", "Courier New", serif;
    font-weight: 700;
    font-size: 27px;
    letter-spacing: 3px;
    fill: var(--ink);
  }
  .seg-red { fill: var(--red); }
  .seg-orange { fill: var(--orange); }
  .seg-green { fill: var(--green); }
  .seg-teal { fill: var(--teal); }
  .seg-shadow-red { fill: var(--red-shade); }
  .seg-shadow-green { fill: var(--green-shade); }
  .seg-shadow-teal { fill: var(--teal-shade); }
  .stage-tile { fill: var(--tile); }
  .icon-fill { fill: var(--ink); }
  .icon-line { fill: none; stroke: var(--ink); stroke-linecap: round; stroke-linejoin: round; }
</style>
</head>
<body>
<svg class="journey-canvas" viewBox="0 0 1500 1000" xmlns="http://www.w3.org/2000/svg" role="img" aria-label="Customer journey: seven stages surrounded by four growth concepts">
  <defs>
    <path id="arc-unique-outer" d="M477,454 A292,292 0 0 1 865,231"/>
    <path id="arc-unique-inner" d="M511,460 A258,258 0 0 1 853,263"/>
    <path id="arc-business-outer" d="M815,219 A290,290 0 0 1 1051,555"/>
    <path id="arc-business-inner" d="M809,254 A255,255 0 0 1 1016,549"/>
    <path id="arc-gameplan" d="M1011,571 A255,255 0 0 1 699,751"/>
    <path id="arc-inside-outer" d="M701,783 A285,285 0 0 1 487,441"/>
    <path id="arc-inside-inner" d="M709,749 A250,250 0 0 1 521,449"/>
  </defs>

  <!-- Concept ring -->
  <g class="concept-ring">
    <path class="seg-teal" d="M598,793 A333,333 0 0 1 443,419 L567,452 A205,205 0 0 0 663,683 Z"/>
    <path class="seg-shadow-green" d="M1067,646 L1090,575 L1025,665 Z"/>
    <path class="seg-shadow-teal" d="M640,780 L700,830 L765,870 Z"/>
    <path class="seg-green" d="M1067,646 A333,333 0 0 1 765,838 L765,888 L625,770 L765,650 L765,710 A205,205 0 0 0 951,592 Z"/>
    <path class="seg-orange" d="M932,217 A333,333 0 0 1 1098,505 L1120,505 L1025,650 L910,505 L970,505 A205,205 0 0 0 867,327 Z"/>
    <path class="seg-red" d="M452,391 A333,333 0 0 1 765,172 L765,120 L900,238 L765,355 L765,300 A205,205 0 0 0 572,435 Z"/>
    <path class="seg-shadow-red" d="M440,420 L505,350 L515,365 L452,430 Z"/>
    <path class="seg-teal" d="M443,419 L409,410 L515,365 L601,461 L567,452 Z"/>
  </g>

  <!-- Concept labels -->
  <text class="concept-label"><textPath href="#arc-unique-outer" startOffset="50%" text-anchor="middle">UNIQUE</textPath></text>
  <text class="concept-label"><textPath href="#arc-unique-inner" startOffset="50%" text-anchor="middle">ADVANTAGE</textPath></text>
  <text class="concept-label"><textPath href="#arc-business-outer" startOffset="50%" text-anchor="middle">BUSINESS</textPath></text>
  <text class="concept-label"><textPath href="#arc-business-inner" startOffset="50%" text-anchor="middle">MODEL</textPath></text>
  <text class="concept-label"><textPath href="#arc-gameplan" startOffset="50%" text-anchor="middle">GAMEPLAN</textPath></text>
  <text class="concept-label"><textPath href="#arc-inside-outer" startOffset="50%" text-anchor="middle">INSIDE OUT</textPath></text>
  <text class="concept-label"><textPath href="#arc-inside-inner" startOffset="50%" text-anchor="middle">THINKING</textPath></text>

  <!-- Stage tiles -->
  <g class="stage stage-target" transform="translate(80,415)">
    <title>Target</title>
    <rect class="stage-tile" width="150" height="150"/>
    <circle class="icon-line" cx="75" cy="75" r="56" stroke-width="10"/>
    <circle class="icon-line" cx="75" cy="75" r="33" stroke-width="10"/>
    <circle class="icon-fill" cx="75" cy="75" r="13"/>
  </g>

  <g class="stage stage-attract" transform="translate(292,415)">
    <title>Attract</title>
    <rect class="stage-tile" width="150" height="150"/>
    <path class="icon-fill" d="M33,45 H57 V92 A18,18 0 0 0 93,92 V45 H117 V92 A42,42 0 0 1 33,92 Z"/>
    <rect class="stage-tile" x="33" y="55" width="24" height="5"/>
    <rect class="stage-tile" x="93" y="55" width="24" height="5"/>
    <polygon class="icon-fill" points="78,12 66,48 77,48 70,78 88,40 78,40 86,12"/>
  </g>

  <g class="stage stage-nurture" transform="translate(492,422)">
    <title>Nurture</title>
    <rect class="stage-tile" width="150" height="150"/>
    <path class="icon-fill" d="M72,88 C50,80 42,55 50,22 C72,38 80,62 72,88 Z"/>
    <path class="icon-fill" d="M80,90 C82,66 94,48 112,40 C114,64 104,84 80,90 Z"/>
    <path class="icon-fill" d="M76,95 C76,70 84,50 96,30 C104,52 96,78 76,95 Z"/>
    <path class="icon-fill" d="M18,118 L40,100 C46,96 52,95 58,96 L88,98 C95,98 95,108 88,108 L66,108 L98,110 L126,96 C132,93 137,100 132,104 L104,124 C98,128 92,130 84,130 L44,128 L30,138 Z"/>
  </g>

  <g class="stage stage-convert" transform="translate(704,425)">
    <title>Convert</title>
    <rect class="stage-tile" width="150" height="150"/>
    <path class="icon-line" d="M42,108 A44,44 0 0 1 97,33" stroke-width="15"/>
    <polygon class="icon-fill" points="90,14 122,38 84,52"/>
    <path class="icon-line" d="M108,42 A44,44 0 0 1 53,117" stroke-width="15"/>
    <polygon class="icon-fill" points="60,136 28,112 66,98"/>
  </g>

  <g class="stage stage-maximise" transform="translate(917,425)">
    <title>Maximise</title>
    <rect class="stage-tile" width="150" height="150"/>
    <rect class="icon-fill" x="20" y="118" width="22" height="24"/>
    <rect class="icon-fill" x="50" y="100" width="22" height="42"/>
    <rect class="icon-fill" x="80" y="72" width="22" height="70"/>
    <rect class="icon-fill" x="110" y="40" width="22" height="102"/>
    <path class="icon-line" d="M22,98 C58,80 82,56 108,24" stroke-width="6"/>
    <polygon class="icon-fill" points="122,10 120,40 96,22"/>
  </g>

  <g class="stage stage-loyalty" transform="translate(1115,427)">
    <title>Loyalty</title>
    <rect class="stage-tile" width="150" height="150"/>
    <polygon class="icon-fill" points="0,48 16,40 30,76 12,84"/>
    <polygon class="icon-fill" points="150,50 134,42 120,78 138,86"/>
    <path class="icon-fill" d="M28,50 L58,48 L78,56 L98,48 L124,52 L118,80 L96,104 C92,110 84,112 80,108 C76,114 68,114 64,108 C58,112 52,110 50,104 C44,106 38,100 42,94 L32,82 Z"/>
    <path class="icon-line" d="M62,64 L84,60 L110,82 M66,94 L74,102 M76,88 L86,98 M86,82 L96,92" stroke="#553f3b" stroke-width="4"/>
  </g>

  <g class="stage stage-reactivation" transform="translate(1296,425)">
    <title>Reactivation</title>
    <rect class="stage-tile" width="150" height="150"/>
    <path class="icon-line" d="M82,34 A44,44 0 1 1 38,82" stroke-width="10" stroke-linecap="butt"/>
    <polygon class="icon-fill" points="50,28 86,12 86,52"/>
  </g>
</svg>
</body>
</html>
```